business card with 2 locations on 1 card

I need a modern looking business card that I would use at 2 different locations. Possibly 1 location on 1 side and other location on other side. One should be able to distinguish the 2 locations immediately before having to read the address or description on card. You can take a look at my website to see what I'm drawn to. The logo is brand new that I just purchased on Pixel Harbor. I want to emphasize family.
Updates

Let's not use the yellow and blue colors. Added Thursday, August 31, 2017

Target Market(s)

women and children

Industry/Entity Type

Health And Wellness

Contact Information for Business Card

Business name: Willow Nest Chiropractic & Acupuncture
My name: Delsa Brook
Job title: DC, MAOM, LAc (CA), CNS

Location 1
Address: 4817 Marlowe Blvd, Suite C-200, Frisco, TX 75036
Phone: (469) 555-0182
Fax: (972) 555-0147

Location 2
Address: 1786 Tenley Road, Suite 300, Plano, TX 75079
Phone: (469) 555-0195
Fax: (972) 555-0147

Email: drdelsabrook@mailvex.example
Website: www.drdelsabrook.example

Font styles to use
Serif
Sans Serif

Colors

Designer to choose colors to be used in the design.

Requirements
Must have
• distinction between 2 locations.
Nice to have
• Colors preference below is there. But I like to see what you come up with too!

```html
<!DOCTYPE html>
<html lang="en">
<head>
<meta charset="utf-8">
<title>Willow Nest Chiropractic &amp; Acupuncture — Business Card</title>
<link href="https://fonts.googleapis.com/css2?family=Cinzel:wght@400;500&family=Source+Sans+3:wght@400;600&display=swap" rel="stylesheet">
<style>
  :root {
    --backdrop: #c9c9c9;
    --card-white: #ffffff;
    --brand-green: #0b8a27;
    --brand-teal: #1f6469;
    --text-grey: #4a4a4a;
    --accent-lime: #d9efa6;
    --divider: #7fa9ac;
  }
  * { margin: 0; padding: 0; box-sizing: border-box; }
  html, body { width: 1200px; height: 900px; overflow: hidden; }
  body {
    background: var(--backdrop);
    position: relative;
    font-family: "Source Sans 3", Arial, sans-serif;
  }
  .card {
    position: absolute;
    top: 307px;
    width: 440px;
    height: 271px;
    border-radius: 12px;
    overflow: hidden;
  }
  .card-front { left: 150px; background: var(--card-white); }
  .card-back { left: 609px; background: var(--brand-green); }

  /* brand block */
  .brand-mark {
    position: absolute;
    left: 60px; top: 51px;
    width: 98px; height: 98px;
    border: 9px solid var(--brand-teal);
    border-radius: 50%;
  }
  .brand-name {
    position: absolute;
    left: 0; width: 218px; top: 150px;
    text-align: center;
    font-family: "Cinzel", "Times New Roman", serif;
    color: var(--brand-teal);
    font-weight: 500;
  }
  .brand-name .primary { display: block; font-size: 27px; line-height: 30px; letter-spacing: 0.5px; }
  .brand-name .secondary { display: block; font-size: 10.5px; line-height: 13px; letter-spacing: 0.2px; }

  .divider {
    position: absolute;
    left: 219px; top: 50px;
    width: 1px; height: 140px;
    background: var(--divider);
  }

  /* contact block */
  .contact { position: absolute; left: 243px; top: 46px; color: var(--text-grey); }
  .person-name {
    font-family: "Cinzel", "Times New Roman", serif;
    font-size: 17px; line-height: 20px;
    color: var(--brand-teal);
    font-weight: 500;
    letter-spacing: 0.5px;
  }
  .credentials { font-size: 12px; line-height: 15px; margin-bottom: 4px; }
  .contact-line {
    display: flex; align-items: flex-start;
    font-size: 12px; line-height: 16px;
  }
  .contact-line svg { flex: none; width: 9px; height: 9px; margin: 3.5px 4px 0 0; fill: var(--brand-teal); }
  .contact-line.gap { margin-top: 9px; }

  /* location band */
  .location-band {
    position: absolute; left: 0; bottom: 0;
    width: 100%; height: 65px;
    background: var(--brand-green);
    color: #ffffff;
    text-align: center;
    padding-top: 15px;
    font-size: 12px; line-height: 19px;
  }
  .band-phones { display: flex; justify-content: center; gap: 14px; }
  .band-phones span { display: inline-flex; align-items: center; }
  .band-phones svg { width: 9px; height: 9px; margin-right: 4px; fill: var(--accent-lime); }

  .back-mark {
    position: absolute;
    left: 330px; top: 137px;
    width: 40px; height: 40px;
    border-radius: 50%;
    background: #ffffff;
  }
</style>
</head>
<body>

<section class="card card-front" aria-label="Business card front">
  <div class="brand-mark"></div>
  <div class="brand-name">
    <span class="primary">Willow Nest</span>
    <span class="secondary">Chiropractic &amp; Acupuncture</span>
  </div>

  <div class="divider"></div>

  <div class="contact">
    <div class="person-name">DELSA BROOK</div>
    <div class="credentials">DC, MAOM, LAc (CA), CNS</div>
    <div class="contact-line">
      <svg viewBox="0 0 10 10"><rect x="0" y="1.5" width="10" height="7" rx="1"/><path d="M0.5 2 L5 5.5 L9.5 2" stroke="#fff" stroke-width="1" fill="none"/></svg>
      <span>drdelsabrook@mailvex.example</span>
    </div>
    <div class="contact-line">
      <svg viewBox="0 0 10 10"><circle cx="5" cy="5" r="5"/><path d="M0 5 H10 M5 0 V10" stroke="#fff" stroke-width="0.8"/></svg>
      <span>www.drdelsabrook.example</span>
    </div>
    <div class="contact-line gap">
      <svg viewBox="0 0 10 10"><path d="M5 0 C2.2 0 1 2 1 3.8 C1 6.5 5 10 5 10 C5 10 9 6.5 9 3.8 C9 2 7.8 0 5 0 Z"/><circle cx="5" cy="3.8" r="1.5" fill="#fff"/></svg>
      <span>4817 Marlowe Blvd,<br>Suite C-200, Frisco, TX 75036</span>
    </div>
    <div class="contact-line">
      <svg viewBox="0 0 10 10"><path d="M2 0.5 L3.8 2.8 L2.8 4 C3.5 5.6 4.6 6.7 6 7.3 L7.2 6.2 L9.5 8 L8.3 9.5 C4.5 9 1 5.5 0.5 1.7 Z"/></svg>
      <span>(469) 555-0182</span>
    </div>
    <div class="contact-line">
      <svg viewBox="0 0 10 10"><rect x="2.5" y="0.5" width="5" height="3"/><rect x="0.5" y="3.5" width="9" height="6" rx="1"/><rect x="2.5" y="6" width="5" height="1" fill="#fff"/></svg>
      <span>(972) 555-0147</span>
    </div>
  </div>

  <div class="location-band">
    <div>1786 Tenley Road, Suite 300, Plano, TX 75079</div>
    <div class="band-phones">
      <span><svg viewBox="0 0 10 10"><path d="M2 0.5 L3.8 2.8 L2.8 4 C3.5 5.6 4.6 6.7 6 7.3 L7.2 6.2 L9.5 8 L8.3 9.5 C4.5 9 1 5.5 0.5 1.7 Z"/></svg>(469) 555-0195</span>
      <span><svg viewBox="0 0 10 10"><rect x="2.5" y="0.5" width="5" height="3"/><rect x="0.5" y="3.5" width="9" height="6" rx="1"/></svg>(972) 555-0147</span>
    </div>
  </div>
</section>

<section class="card card-back" aria-label="Business card back">
  <div class="back-mark"></div>
</section>

</body>
</html>
```